Real eatate

My company name is “Maple Crest Realestate” i would like to create a business card. I would like something modern and sleek similar to picture uploaded. All text in the business card should be black and the logo gold any shade.

```html
<!DOCTYPE html>
<html lang="en">
<head>
<meta charset="utf-8">
<title>Maple Crest Realestate – Business Card</title>
<link rel="stylesheet" href="https://fonts.googleapis.com/css2?family=Oswald:wght@500&family=Arimo:wght@400&display=swap">
<style>
  :root {
    --backdrop: #b3b3b3;
    --gold-top: #fcc303;
    --gold-bottom: #fba80a;
    --gold: #fbb50c;
    --ink: #111111;
    --rule: #9a9a9a;
    --paper: #ffffff;
  }
  * { margin: 0; padding: 0; box-sizing: border-box; }
  html, body { width: 1200px; height: 1200px; overflow: hidden; }
  body {
    background: var(--backdrop);
    position: relative;
    font-family: "Arimo", Arial, sans-serif;
  }
  .card {
    position: absolute;
    top: 303px;
    height: 594px;
    box-shadow: 3px 4px 6px rgba(0,0,0,0.45);
  }
  .card-front {
    left: 200px;
    width: 370px;
    background: linear-gradient(180deg, var(--gold-top), var(--gold-bottom));
  }
  .card-back {
    left: 599px;
    width: 364px;
    background: var(--paper);
  }
  .front-brand {
    position: absolute;
    left: 0; right: 0; top: 228px;
    display: flex; flex-direction: column; align-items: center; gap: 14px;
  }
  .brand-dot {
    width: 46px; height: 46px; border-radius: 50%;
    background: var(--paper);
  }
  .front-name {
    font-family: "Oswald", "Arial Narrow", sans-serif;
    font-weight: 500;
    font-size: 40px;
    line-height: 1;
    color: var(--paper);
    letter-spacing: 1px;
  }
  .front-web {
    position: absolute;
    left: 0; right: 0; top: 530px;
    text-align: center;
    font-size: 17px;
    color: var(--paper);
  }
  .back-brand {
    position: absolute;
    left: 0; right: 0; top: 62px;
    display: flex; flex-direction: column; align-items: center;
  }
  .back-brand .brand-dot {
    background: var(--gold);
    width: 58px; height: 58px;
    margin-bottom: 40px;
  }
  .back-name {
    font-family: "Oswald", "Arial Narrow", sans-serif;
    font-weight: 500;
    color: var(--gold);
    text-align: center;
    line-height: 1;
  }
  .back-name .line-main { display: block; font-size: 42px; }
  .back-name .line-sub { display: block; font-size: 16px; letter-spacing: 9px; margin-top: 8px; padding-left: 9px; }
  .person {
    position: absolute; left: 0; right: 0; top: 296px;
    text-align: center;
  }
  .person-name {
    font-family: "Oswald", "Arial Narrow", sans-serif;
    font-weight: 500;
    font-size: 33px;
    line-height: 1;
    color: var(--ink);
  }
  .person-title {
    font-size: 18px;
    color: var(--ink);
    margin-top: 3px;
  }
  .icon-row {
    position: absolute; left: 87px; right: 87px; top: 365px;
    display: flex; align-items: center; gap: 4px;
  }
  .icon-row .rule { flex: 1; height: 1px; background: var(--rule); margin: 0 2px; }
  .icon {
    width: 25px; height: 25px; border-radius: 4px;
    background: var(--gold);
    display: flex; align-items: center; justify-content: center;
  }
  .contacts {
    position: absolute; left: 0; right: 0; top: 398px;
    text-align: center;
    font-size: 17px;
    line-height: 21.5px;
    color: var(--ink);
  }
  .divider {
    position: absolute; left: 88px; right: 80px; top: 496px;
    height: 1px; background: var(--rule);
  }
  .address {
    position: absolute; left: 0; right: 0; top: 508px;
    text-align: center;
    font-size: 17px;
    line-height: 21.5px;
    color: var(--ink);
  }
</style>
</head>
<body>
  <section class="card card-front">
    <div class="front-brand">
      <div class="brand-dot"></div>
      <div class="front-name">MAPLE CREST</div>
    </div>
    <p class="front-web">WWW.MAPLECREST.COM</p>
  </section>

  <section class="card card-back">
    <div class="back-brand">
      <div class="brand-dot"></div>
      <div class="back-name">
        <span class="line-main">MAPLE CREST</span>
        <span class="line-sub">REALESTATE</span>
      </div>
    </div>

    <div class="person">
      <div class="person-name">DANIEL HARPER</div>
      <div class="person-title">Managing Director</div>
    </div>

    <div class="icon-row">
      <span class="rule"></span>
      <span class="icon" aria-label="Phone">
        <svg width="15" height="15" viewBox="0 0 16 16"><path d="M2 5c0-2 2-3 6-3s6 1 6 3l-3 1-1-2H6L5 6 2 5zM4 7h8l1 6H3l1-6z" fill="#fff"/></svg>
      </span>
      <span class="icon" aria-label="Mobile">
        <svg width="15" height="15" viewBox="0 0 16 16"><rect x="4" y="1" width="8" height="14" rx="1.5" fill="none" stroke="#fff" stroke-width="1.5"/><circle cx="8" cy="12.5" r="0.9" fill="#fff"/></svg>
      </span>
      <span class="icon" aria-label="Email">
        <svg width="15" height="15" viewBox="0 0 16 16"><rect x="1.5" y="3.5" width="13" height="9" fill="none" stroke="#fff" stroke-width="1.3"/><path d="M1.5 3.5 8 9l6.5-5.5" fill="none" stroke="#fff" stroke-width="1.3"/></svg>
      </span>
      <span class="icon" aria-label="Location">
        <svg width="15" height="15" viewBox="0 0 16 16"><path d="M8 1a4.5 4.5 0 0 0-4.5 4.5C3.5 9 8 15 8 15s4.5-6 4.5-9.5A4.5 4.5 0 0 0 8 1z" fill="#fff"/><circle cx="8" cy="5.5" r="1.7" fill="#fbb50c"/></svg>
      </span>
      <span class="rule"></span>
    </div>

    <div class="contacts">
      <p>044-123 456 789</p>
      <p>044-123 456 789</p>
      <p>info@maplecrest.com</p>
      <p>www.maplecrest.com</p>
    </div>

    <div class="divider"></div>

    <div class="address">
      <p>421, Address line here</p>
      <p>45452,Country Name</p>
    </div>
  </section>
</body>
</html>
```